Full revamp of cheap website design - the best designer will be offered a much larger project!

Corwell Tane are a progressive and innovative mid-tier professional services group (accountants and business advisors) with offices based in major cities throughout Australia and New Zealand.
Our positioning statement is "Energetic, Innovative, Streetwise", and the visual appearance must reflect this. Although still a relatively conservative industry, we aim to project a modern, innovative, energetic, highly professional but approachable image. The presentation should tie in with the theme "we take our work seriously, not ourselves".
Our aim with this new design is the elevate the status of the group in its online presentation and communication... we want to 'impress' and stand out from the crowd! See our existing site at www.corwelltane.com.au
We're looking for a special designer to take on the Web Site Design Concept - Uncoded - graphics only in line with the concept architecture we will provide (although we are flexible with the layout - we want an interface design that works!). Must work within the constraints of a suitable wordpress theme... Designer to source (we quite like thembrova.com as an option, but havn't seen any really slick representations of it)... there are many other great themes to choose from). Must include a series of slick flash banner designs.
or alternatively,
Design and coding (custom design theme) using wordpress platform (unless you can convince us of the benefits of using some other recognised and supported platform).
Happy to receive the design concepts as graphics only (but the flash is an important factor). You'll need to prove that it will work within an existing theme (or that you are capable of quickly developing a bug-free custom site on the wordpress platform.
Only highly talented and professional designers need enter, but the right designer will be well rewarded with the offer of a much larger design project and plenty of ongoing work.
Task
We are completely overhauling our existing and outdated website(s) x 9 and are looking for a new visual design concept (homepage plus one inside section homepage, one information page and one state homepage to start).
Once our executive have selected and approved the winning concept, we will offer you the opportunity to complete all other sections of the site including a variety of flash banners and other visual section headings, advertising and promotional pieces not only for the central corwelltane.com.au site, but for all of the state sites (8), which will replicate the central site with mainly banner and advertising changes. We will look after content entry.
This project will grow into quite a large opportunity for the right designer with ongoing design elements in the form of flash banners, banner ads, newsletter and other emarketing designs, plus related blogs and product sites required over time.
We will provide you with a flexible wireframe architecture from which to work, along with conceptual content and imagery where available (feel free to use stock images wherever necessary). If you need something else, just ask!
Deadline
Unfortunately, we need you to work to a ridiculously tight deadline on the concept design, due to a pending executive meeting (where we are committed to making a decision on the approved concept). We need your designs to be submitted by 3/11/2009. The good news is that we can get started on the full project reasonably quickly following the first deadline.
Some of our competitors:
www.lindqvistmoray.com.au
www.quillan.com.au
www.tessaly.com.au
www.zvr.com.au
www.gae.com.au
www.edgarmolloy.com.au
www.vantro.com.au
www.pellinggroup.com.au
www.tzr.com.au
www.glund.com
You'll need to contact me at renatao@corwelltane.net so that I can give you access to the resources you'll need to get the conceptual design job done. Just send me a quick note letting me know that you're interested in the contest.
Updates
Hello to all Corwell Tane website redesign competitors!
A quick hello to all our competitors!
Thank you for submitting your fabulous designs... I will be looking at each of them tomorrow (PM) and will provide you with individual feedback and in some cases, requests for minor modifications prior to our Executive presentation on the 6th. Once again, I do apologise for the delay in my response and the rush required at your end.
Many thanks
Renata
Hello,
I have extended the deadline via ArtQuarry to enable you to make the requested changes and get them back to me asap TODAY!
Although I only extended the deadline by 1 day, it is now showing as almost 2 days left. This is not the case. I MUST have your revised designs as soon as possible TODAY.
Many thanks for your great work!
Renata
Hi!
Hello Art Quarry Contestants!
I'm terribly sorry about the delay... still waiting on the OK from our Senior Executive members on which design we will pursue. I am chasing an answer and will get back to you as soon as possible.
Many thanks for your patience.
Renata
Target Market(s)
Our primary target is the mid-size SME marketplace with turnover $5 - $50mil (CFO, COO, MD, GM - ie, Senior Executives) plus High Net worth individuals and high quality staff.
Corwell Tane's target market are clients who have (and are) invested in their businesses and/or themselves but now need our assistance to grow and develop further.
They need accountants and advisers who can deliver more than the fundamentals. Our clients are defined by an attitude that motivates them to seek out opportunities while putting the structures in place to ensure the security of their futures.
Number of Pages Required
4 pages
Requirements
Must have
- Designs must be clean and uncluttered whilst maintaining a slick and professional yet approachable look and feel.
The corporate logo must be used and unchanged.
A series of attractive, text based flash animated banners will be required to highlight our key messaging
All of the page components as outlined in the concept design provided are required (although layout and other suggested modifications are welcomed).
As noted earlier, you need to contact me at renatao@corwelltane.net so that I can give you access to the resources you''ll need to get the conceptual design job done. Just send me a quick note letting me know that you''re interested in the content.
Nice to have
- If possible (although not absolutely necessary), consideration should be made regarding tying in our NZ member firm''s site design at www.corwelltane.co.nz (which will not change) along with www.veldrinalliance.com. Although we don''t wish to replicate either of these designs, it would be nice to somehow connect them visually in some way. Certainly the site map at the bottom of the page (like the NZ site) must be maintained.
If you want to chat through the brief you are welcome to call or IM me on skype: renata.oblomova
Should not have
- images of abacus''s!

```html
<!DOCTYPE html>
<html lang="en">
<head>
<meta charset="utf-8">
<title>Corwell Tane – About Us</title>
<link href="https://fonts.googleapis.com/css2?family=PT+Sans:wght@400;700&family=Open+Sans:wght@400;600;700&display=swap" rel="stylesheet">
<style>
:root{
  --slate:#4a5563;
  --blue:#3b9fdc;
  --blue-dark:#2e6fb5;
  --band:#dcebf5;
  --band-line:#c6dcec;
  --rule:#bcd9ec;
  --text:#3a3a3a;
  --footer-text:#e6ebf0;
}
*{box-sizing:border-box;margin:0;padding:0}
html,body{width:1200px;height:2341px;overflow:hidden;background:#fff}
body{position:relative;font-family:"PT Sans",sans-serif;color:var(--text);font-size:12.5px}
a{color:inherit;text-decoration:none}
.abs{position:absolute}

.topbar{left:0;top:0;width:1200px;height:13px;background:var(--slate)}
.search{left:732px;top:12px;width:329px;height:28px;background:var(--slate);border-radius:0 0 4px 4px;display:flex;align-items:center;padding:0 8px 0 13px;gap:10px;color:#fff;font:11px "Open Sans",sans-serif}
.search .field{flex:1;height:16px;background:#fff}
.search .go{width:18px;height:18px;border-radius:50%;background:var(--blue);display:flex;align-items:center;justify-content:center}

.brand{left:94px;top:47px;display:flex;align-items:center;height:72px}
.brand .mark{width:34px;height:34px;background:var(--blue-dark);margin-right:26px;margin-left:12px}
.brand .divider{width:1px;height:66px;background:#d4d4d4;margin-right:18px}
.brand .name{font:400 28px "Open Sans",sans-serif;color:#5b6470;letter-spacing:.3px}

.nav{left:422px;top:74px;width:641px;height:46px;border-bottom:1px solid var(--rule);display:flex;font:10.5px "Open Sans",sans-serif;color:#222}
.nav a{padding:0 16px;line-height:16px;position:relative}
.nav a.active{color:var(--blue);font-weight:600}
.nav a.active::after{content:"";position:absolute;left:0;right:0;top:44px;height:3px;background:var(--blue)}
.header-rule{left:0;top:151px;width:1200px;height:1px;background:var(--band-line)}

.banner{left:0;top:154px;width:1200px;height:282px;background:var(--band);border-bottom:2px solid var(--band-line)}
.photo{background:linear-gradient(135deg,#5f86a8,#27466a);border:2px solid #fff}
.photo.suits{background:linear-gradient(180deg,#eef1f4,#8a94a2)}
.banner-title{left:669px;top:165px;font:400 29px "Open Sans",sans-serif;color:#4a5563}
.banner-lead{left:672px;top:209px;width:378px;font:400 17px/26px "PT Sans",sans-serif;color:var(--blue);text-align:justify}
.banner-sub{left:673px;top:318px;width:377px;font:15px/24px "PT Sans",sans-serif;color:#444}
.pager{left:933px;top:396px;display:flex;gap:9px}
.pager span{width:22px;height:22px;border:2px solid #333;border-radius:50%;font:12px/18px "Open Sans",sans-serif;text-align:center;color:#333}
.pager span.on{border-color:var(--blue);color:var(--blue)}

.crumb{left:92px;top:461px;width:724px;height:34px;border-bottom:1px solid var(--rule);font:15px "PT Sans",sans-serif;color:#444}
.crumb b{color:var(--blue);font-weight:700}
.crumb i{font-style:normal;margin:0 10px 0 14px}

.content{left:95px;top:500px;width:724px;font-size:12.8px;letter-spacing:.2px;line-height:20.8px;color:#333;text-align:justify}
.content h2{font:400 20px "Open Sans",sans-serif;letter-spacing:0;color:var(--blue);margin-bottom:18px}
.content h3{font-size:12.8px;font-weight:700;color:var(--blue);margin-bottom:20.8px}
.content p{margin-bottom:20.8px}
.content .tight{margin-bottom:0}
.content a{color:var(--blue);font-weight:700;text-decoration:underline}

.card{border:1px solid var(--rule);padding:3px}
.card .head{height:34px;background:var(--band);font:700 12.5px/34px "PT Sans",sans-serif;color:var(--blue);padding-left:14px}
.card .pic{height:130px;background:linear-gradient(135deg,#5a5e66,#b58a6a)}
.card .pic.hands{background:linear-gradient(135deg,#7a6a5c,#3e5a7a)}
.card .pic.net{background:linear-gradient(135deg,#f1f4f7,#b8cde0)}
.blurb{font-size:12.5px;letter-spacing:.2px;line-height:20.8px;color:#333;text-align:justify}
.pill{height:23px;border-radius:12px;background:var(--blue);color:#fff;font:700 11.5px/23px "PT Sans",sans-serif;padding:0 28px 0 10px;position:absolute}
.pill::after{content:"";position:absolute;right:3px;top:3px;width:15px;height:15px;border:2px solid #fff;border-radius:50%}
.pill::before{content:"";position:absolute;right:9px;top:8px;border-left:5px solid #fff;border-top:4px solid transparent;border-bottom:4px solid transparent}

.side{left:837px;top:459px;width:226px}
.side h4{font:400 18px "Open Sans",sans-serif;color:var(--blue);padding-bottom:10px;border-bottom:1px solid var(--rule);margin-bottom:14px}
.quote{font-style:italic;font-size:12.3px;line-height:20.8px;color:#555;text-align:justify}
.quote-by{font-size:12.3px;line-height:20.8px;font-weight:700;margin-bottom:16px}
.news{position:relative;font-size:12.5px;line-height:20.8px;height:149px}
.news strong{color:#333}
.news .cat{color:var(--blue);font-size:12px;letter-spacing:.4px}
.news .pill{right:0;bottom:-1px;padding-right:30px;padding-left:13px}

.footer{left:0;top:1980px;width:1200px;height:361px;background:var(--slate);color:var(--footer-text);font-size:11.5px;line-height:20.8px}
.fcol{position:absolute;top:22px}
.fcol h5{font:700 14.5px "PT Sans",sans-serif;color:#fff;margin-bottom:12px}
.fcol .hl{color:var(--blue);font-weight:700}
.fcol .mail{color:var(--blue)}
.contact{line-height:18.7px}
.contact h5{margin-bottom:14px}
.footer .rule{position:absolute;left:121px;top:291px;width:968px;height:1px;background:var(--blue)}
.footer .copy{position:absolute;left:129px;top:314px}
.footer .links{position:absolute;right:121px;top:314px;display:flex;gap:19px}
.arrows{position:absolute;left:1002px;top:243px;display:flex;align-items:center;gap:8px}
.arrows span{width:18px;height:18px;border:2px solid #fff;border-radius:50%}
.arrows i{width:1px;height:22px;background:#fff}
</style>
</head>
<body>
<div class="abs topbar"></div>
<div class="abs search">SEARCH<span class="field"></span><span class="go"><svg width="8" height="8" viewBox="0 0 8 8"><path d="M2 1l5 3-5 3z" fill="#fff"/></svg></span></div>

<div class="abs brand"><span class="mark"></span><span class="divider"></span><span class="name">Corwell Tane</span></div>
<nav class="abs nav">
  <a class="active" href="#">HOME</a><a href="#">CLIENT LOGIN</a><a href="#">ABOUT</a><a href="#">SERVICES</a><a href="#">OUR NETWORK</a><a href="#">INFOTELLIGENCE</a><a href="#">CONTACT</a>
</nav>
<div class="abs header-rule"></div>

<section class="abs banner"></section>
<div class="abs photo" style="left:93px;top:171px;width:369px;height:245px" role="img" aria-label="Many hands joined together in a circle"></div>
<div class="abs photo suits" style="left:470px;top:168px;width:186px;height:248px" role="img" aria-label="Group of business professionals standing together"></div>
<h1 class="abs banner-title">Our Network</h1>
<p class="abs banner-lead">Through our member firms, Corwell Tane Employs and nurtures the intellectual capital of over 600 talented and professional people across Australia and New Zealand</p>
<p class="abs banner-sub">Our strong network enables our member firms to better deliver both breadth and depth of specialisation, industry and local experience when required.</p>
<div class="abs pager"><span class="on">1</span><span>2</span><span>3</span><span>4</span></div>

<div class="abs crumb">Home<i>&gt;</i><b>About Us</b></div>

<main class="abs content">
  <h2>Where to Next?</h2>
  <p>This is what we're asked by many people and the reason why our clients chose Corwell Tane.</p>
  <p class="tight">Our clients know we are good at the fundamentals - accounting, tax compliance, and audit – but they come to us because not only are we good at the fundamentals, we have the expertise to help them identify, structure, and secure, their future…their next step. Whether you are a business owner or operator, or someone looking to seize the opportunities personally available to you, we can help.</p>
  <p>With a broad range of <a href="#">services</a> and <a href="#">solutions</a>, Corwell Tane can help you achieve your next step.</p>
  <h3>Our structure</h3>
  <p>Corwell Tane is an association (or federation?) of independent accounting firms across Australia and New Zealand (link). While we are united by a common culture and brand, each Corwell Tane firm is independent. The team that run the firm, own the business and have a special interest in making sure that they deliver what clients need and an understanding of what it takes to succeed.</p>
  <h3>Our reach</h3>
  <p>Corwell Tane is an independent member of <a href="#">Veldrin Alliance</a>, a global association of 78 independent professional services firms covering accounting, audit, tax, business consulting and legal in 54 countries around the world.</p>
  <p>We know that nothing beats good local knowledge and representation to move things along and achieve the right results when you're operating across borders. Our connections through the Veldrin Alliance group are strong and ensure that, regardless of where you or your business need to go, we can offer you a professional and streamlined service.</p>
  <h3>Our history</h3>
  <p>Represented by eight firms across Australia and New Zealand with (?) directors and over (?) professional staff, the Corwell Tane group is large enough to offer high level support and an impressive breadth of expertise, but small enough to give clients the individual attention they need.</p>
  <p>Like many businesses, our origins were small. Back in the early 1970s when flares were popular and the Kestrel/Marlow debate was in full swing, Doug Corwell started a one-man practice, DC Corwell &amp; Co, in the Sydney suburb of Ashbourne.</p>
  <p>A partnership, the adoption of the name Corwell Tane, and a new office later, we decided to start practicing the strategies we were teaching our clients. Progressively, Corwell Tane sought out like- minded professionals and in 1996, formed an association of independent accounting and business advisory firms.</p>
  <p>We know that a common culture and common goals are integral to success. All members of the Corwell Tane group have been selected for their technical competency, professional success, 'real world' attitude and approach, client focus, and desire to achieve the right result.</p>
  <p>Bottom line; they're just good people to work with who take their work seriously but not themselves.</p>
</main>

<div class="abs card" style="left:91px;top:1459px;width:237px">
  <div class="head">Our Leaders</div>
  <div class="pic" role="img" aria-label="Senior business leader speaking at a meeting"></div>
</div>
<div class="abs card" style="left:343px;top:1459px;width:235px">
  <div class="head">Our Network</div>
  <div class="pic hands" role="img" aria-label="Hands joined together in a circle"></div>
</div>
<div class="abs card" style="left:591px;top:1459px;width:233px">
  <div class="head">Member Firms</div>
  <div class="pic net" role="img" aria-label="Person drawing a network of connected people"></div>
</div>

<p class="abs blurb" style="left:93px;top:1642px;width:235px">Each partner, each advisor, each member of the Corwell Tane Group has been carefully selected for the range of services and commitment they offer above and beyond the traditional fare.</p>
<p class="abs blurb" style="left:344px;top:1643px;width:234px">As a group, Corwell Tane have access to extended networks and resources both nationally and internationlly, which enable us to provide our clients with the backing of a large firm.</p>
<p class="abs blurb" style="left:592px;top:1644px;width:232px">Our Member firms across Australia and New Zealand are independently operated which means personalised client care and 'real world' understanding of your needs and what it takes to succeed.</p>
<a class="pill" href="#" style="left:110px;top:1762px;width:217px">More about the leadership team</a>
<a class="pill" href="#" style="left:395px;top:1762px;width:183px;padding-left:13px">More about our network</a>

<aside class="abs side">
  <h4>Don't take our word for it!</h4>
  <p class="quote">"Testimonial goes here... testimonial goes here and includes the persons and clients name. Sometimes will link through to a page, but not always. Client name will link to their website."</p>
  <p class="quote-by"><span style="color:var(--blue)">Person's name</span><br>Client name</p>
  <h4>Latest News &amp; Events</h4>
  <div class="news"><strong>Should I increase my prices?</strong><br><span class="cat">Business Scruples Q&amp;A</span><br>The costs of running my business have gone up (despite what they keep telling me on the news) but I have .....<a class="pill" href="#">More</a></div>
  <div class="news"><strong>Should I increase my prices?</strong><br><span class="cat">Business Scruples Q&amp;A</span><br>The costs of running my business have gone up (despite what they keep telling me on the news) but I have .....<a class="pill" href="#">More</a></div>
  <div class="news"><strong>Should I increase my prices?</strong><br><span class="cat">Business Scruples Q&amp;A</span><br>The costs of running my business have gone up (despite what they keep telling me on the news) but I have .....<a class="pill" href="#">More</a></div>
</aside>

<footer class="abs footer">
  <div class="fcol" style="left:128px"><h5>About</h5>Innovative,<br>Energetic,<br>Streetsmart<br>Leadership team</div>
  <div class="fcol" style="left:280px"><h5>Services</h5>Tax sollutions<br>Business sale<br>Audit&amp;Risk<br>Tax sollutions<br>Business sale<br>Audit&amp;Risk</div>
  <div class="fcol" style="left:456px"><h5>Network</h5>Adelaide<br>Brisbane<br>Darwin<br>Perth<br>Sydney<br>Melbourne<br>New Zealand</div>
  <div class="fcol" style="left:619px"><h5>Knowledge</h5>Tax sollutions<br>Business sale<br>Audit&amp;Risk<br>Tax sollutions<br>Business sale<br>Audit&amp;Risk</div>
  <div class="fcol contact" style="left:790px"><h5>Contact</h5><span class="hl">Australia<br>New South Wales</span><br><br>Corwell Tane<br>Level 4, 82 Garnet St&nbsp; Sydney NSW 2000<br><br>GPO Box 7312 Sydney NSW 2001<br><br>Tel: 02 9471 3080<br>Fax: 02 9471 3081<br><span class="mail">E-mail: info@corwelltane.com.au</span></div>
  <div class="arrows"><span></span><i></i><span></span></div>
  <div class="rule"></div>
  <div class="copy">Copyright Corwell Tane 2009t</div>
  <div class="links"><a href="#">Privacy</a><a href="#">Disclaimer</a><a href="#">Subscribe</a><a href="#">Site Manager</a><a href="#">Links</a><a href="#">RSS and other Social media links</a></div>
</footer>
</body>
</html>
```